New Business Card Design Project

Want a simple but attention grabbing business card. Back Side having mainly our logo and basic info-the front side a typical business card.

Contact Information for Business Card

Hearth & Basin Works
218 NW Larkfield Rd. Suite 207
Ankeny, Iowa 50021

phone- 515.284.7093

website is -hbwplains.com

```html
<!DOCTYPE html>
<html lang="en">
<head>
<meta charset="utf-8">
<title>Hearth &amp; Basin Works — Business Card</title>
<link rel="stylesheet" href="https://fonts.googleapis.com/css2?family=Montserrat:wght@500;700&display=swap">
<style>
  :root {
    --navy: #0a1428;
    --orange: #ee5a24;
    --blue: #2372c0;
    --ink: #1a1a1a;
    --paper: #ffffff;
    --stage: #d9d8d4;
  }
  * { box-sizing: border-box; margin: 0; padding: 0; }
  html, body { width: 1200px; height: 875px; overflow: hidden; }
  body {
    background: var(--stage);
    font-family: "Montserrat", Arial, sans-serif;
    display: flex;
    align-items: center;
    justify-content: center;
    gap: 40px;
  }
  .card {
    width: 540px;
    height: 309px;
    position: relative;
    overflow: hidden;
  }
  .card--back {
    background: var(--navy);
    border-bottom: 4px solid var(--orange);
    display: flex;
    align-items: center;
    justify-content: center;
  }
  .brand-name {
    color: var(--orange);
    font-weight: 700;
    font-size: 34px;
    line-height: 1.15;
    text-align: center;
    letter-spacing: 0.5px;
  }
  .card--front {
    background: var(--paper);
    border-left: 3px solid var(--blue);
    border-bottom: 4px solid var(--blue);
  }
  .front-brand {
    position: absolute;
    top: 34px;
    right: 34px;
    color: var(--orange);
    font-weight: 700;
    font-size: 20px;
    line-height: 1.15;
    text-align: right;
  }
  .divider {
    position: absolute;
    left: 70px;
    right: 30px;
    top: 160px;
    height: 1.5px;
    background: var(--orange);
  }
  .accent-bar {
    position: absolute;
    left: 0;
    top: 110px;
    width: 10px;
    height: 42px;
    background: var(--orange);
  }
  .person {
    position: absolute;
    left: 34px;
    top: 108px;
  }
  .person__name {
    color: var(--blue);
    font-weight: 700;
    font-size: 20px;
    letter-spacing: 0.5px;
  }
  .person__role {
    color: var(--ink);
    font-weight: 500;
    font-size: 14px;
    margin-top: 2px;
  }
  .contact {
    position: absolute;
    left: 34px;
    top: 184px;
    list-style: none;
    font-size: 13.5px;
    font-weight: 500;
    color: var(--ink);
  }
  .contact li {
    display: flex;
    align-items: center;
    gap: 9px;
    margin-bottom: 9px;
  }
  .contact svg { width: 13px; height: 13px; fill: var(--orange); flex: none; }
  .address {
    position: absolute;
    right: 34px;
    top: 184px;
    text-align: right;
    font-size: 14px;
    font-weight: 500;
    color: var(--ink);
    line-height: 1.45;
    font-style: normal;
  }
</style>
</head>
<body>
  <section class="card card--back" aria-label="Card back">
    <p class="brand-name">Hearth &amp; Basin<br>Works</p>
  </section>

  <section class="card card--front" aria-label="Card front">
    <p class="front-brand">Hearth &amp; Basin<br>Works</p>
    <span class="accent-bar"></span>
    <div class="person">
      <p class="person__name">DALE RENNICK</p>
      <p class="person__role">CEO &amp; Founder</p>
    </div>
    <span class="divider"></span>
    <ul class="contact">
      <li>
        <svg viewBox="0 0 16 16" aria-hidden="true"><path d="M3 1h3l1.5 4-2 1.3a9 9 0 0 0 4.2 4.2L11 8.5l4 1.5v3a2 2 0 0 1-2 2A12 12 0 0 1 1 3a2 2 0 0 1 2-2z"/></svg>
        515.284.7093
      </li>
      <li>
        <svg viewBox="0 0 16 16" aria-hidden="true"><path d="M1 3h14v10H1z M1 3l7 6 7-6" stroke="#fff" stroke-width="1.2"/></svg>
        info@hbwplains.com
      </li>
      <li>
        <svg viewBox="0 0 16 16" aria-hidden="true"><circle cx="8" cy="8" r="7"/><path d="M1 8h14M8 1c3 3 3 11 0 14M8 1c-3 3-3 11 0 14" stroke="#fff" stroke-width="1" fill="none"/></svg>
        www.hbwplains.com
      </li>
    </ul>
    <address class="address">
      218 NW Larkfield Rd.<br>
      Suite 207 Ankeny, Iowa 50021
    </address>
  </section>
</body>
</html>
```